Website for "Bright Over Dusk Ltd" cleaning bsuiness

We require a website to expose our business to the local market. We want to provide background on who we are and what we do but in an easily digestible way. We clean domestic and commercial premises and want to provide a list of all of our services to potential customers. We operate out of Warrington in the UK.

We would like the website to be animated in some way so that the experience of using it is not dull or mundane. This website needs to be an extension of our company.

Target Market(s)

30 - 60 year olds for Domestic plus commercial clients

Industry/Entity Type

Cleaning Service

Coding

Coded - Design and coding required

Number of Pages Required

4 page

Font styles to use
Sans Serif

Colors
0455a3
3176b5
85acd3
cfdeed
ffffff
000000
1b1b1b
c8c8c8
757575

Requirements
Must have
• Logo which has been provided. Theme based around the logo and its colours. Simple layout to avoid confusion.
Nice to have
• Animations where possible to impress the customer.
Should not have
• any pictures of cleaning equipment, fairies, maids etc

```html
<!DOCTYPE html>
<html lang="en">
<head>
<meta charset="utf-8">
<title>Bright Over Dusk Ltd — Professional Cleaning</title>
<link href="https://fonts.googleapis.com/css2?family=Open+Sans:wght@300;400;600;700&display=swap" rel="stylesheet">
<style>
:root{
  --stage:#3a3a3a;
  --navy:#0455a3;
  --blue:#3176b5;
  --sky:#85acd3;
  --ice:#cfdeed;
  --white:#ffffff;
  --ink:#1b1b1b;
  --line:#c8c8c8;
  --muted:#757575;
  --tint:#f4f7fb;
  --bar:#f1f1f1;
  --bright:#1e88e5;
}
*{margin:0;padding:0;box-sizing:border-box}
html,body{width:1200px;height:1200px;overflow:hidden;background:var(--stage);font-family:"Open Sans",Arial,sans-serif;color:var(--ink)}
.stage{position:absolute;left:0;top:0;width:1500px;height:1500px;transform:scale(.8);transform-origin:0 0}
.page{position:absolute;left:489px;top:0;width:523px;height:1500px;background:var(--white);overflow:hidden}
.abs{position:absolute}
.section{position:absolute;left:0;width:523px}
.tiny{font-size:4px;color:var(--muted);line-height:1.7}
.h-sec{font-size:8px;font-weight:600;letter-spacing:.1px;color:var(--ink)}
.btn{position:absolute;font-size:4.2px;font-weight:700;text-align:center;letter-spacing:.2px}
.btn-solid{background:var(--blue);color:var(--white)}
.btn-line{border:1px solid var(--blue);color:var(--ink);background:var(--white)}
.arrow-box{position:absolute;width:12px;height:12px;border:1px solid var(--blue);background:var(--white);display:flex;align-items:center;justify-content:center}
.ph{position:absolute}

.topbar{top:0;height:20px;background:var(--bar)}
.topbar span{position:absolute;top:8px;font-size:3.8px;color:var(--muted)}
.header{top:20px;height:45px;background:var(--white)}
.brand{position:absolute;left:33px;top:12px;display:flex;align-items:center;gap:4px}
.brand-dot{width:9px;height:9px;border-radius:50%;background:var(--blue)}
.brand-name{font-size:7px;font-weight:600;color:var(--navy);line-height:1.1}
.call{position:absolute;left:410px;top:12px;font-size:3.6px;color:var(--muted)}
.call b{display:block;font-size:6.4px;color:var(--ink);font-weight:600;margin-top:2px}
.nav{top:65px;height:22px;background:var(--blue)}
.nav a{position:absolute;top:8px;font-size:5px;color:var(--white);text-decoration:none;font-weight:600}
.nav a.on{color:var(--ice)}
.hero{top:87px;height:171px;background:linear-gradient(180deg,#52a8ea 0%,#6fbaf0 60%,#8ccaf5 100%)}
.hero h1{position:absolute;left:35px;top:40px;font-size:27px;font-weight:300;color:var(--white);line-height:35px;z-index:2}
.services{top:258px;height:242px;background:linear-gradient(180deg,#fff 70%,#f3f8fd 100%)}
.card{position:absolute;top:52px;height:133px;background:var(--white);border:1px solid #eceff3;box-shadow:0 1px 2px rgba(0,0,0,.05)}
.card p{position:absolute;left:0;right:0;top:93px;text-align:center;font-size:5.4px;color:var(--ink);line-height:1.35}
.welcome{top:500px;height:285px;background:var(--white)}
.welcome h2{position:absolute;left:193px;top:50px;font-size:8px;font-weight:600;color:var(--navy)}
.feat{position:absolute;top:178px;width:90px}
.feat .ic{width:20px;height:20px;background:var(--blue);border-radius:2px 2px 8px 8px;display:flex;align-items:center;justify-content:center}
.feat h4{font-size:4.8px;font-weight:700;margin-top:10px}
.feat p{margin-top:6px}
.staff{top:785px;height:166px;background:var(--tint)}
.industries{top:951px;height:204px;background:var(--white)}
.ind{position:absolute;font-size:4.2px;color:var(--muted);display:flex;align-items:center;gap:5px}
.quote{position:absolute;left:287px;top:64px;width:198px;height:112px;border:1px solid #e3e6ea;background:var(--white)}
.news{top:1155px;height:198px;background:var(--tint)}
.post{position:absolute;top:52px;width:217px;height:116px;background:var(--white);box-shadow:0 1px 3px rgba(0,0,0,.06)}
.post h5{position:absolute;left:12px;top:26px;font-size:4.8px;font-weight:600}
.post .flag{position:absolute;left:1px;top:26px;width:2px;height:6px;background:var(--bright)}
.footer{top:1353px;height:127px;background:var(--ink);color:var(--white)}
.footer h6{position:absolute;top:18px;font-size:5.4px;font-weight:600}
.footer .row{position:absolute;font-size:4.4px;display:flex;gap:6px;align-items:flex-start;line-height:1.5}
.footer .links{position:absolute;left:171px;top:40px;font-size:4.4px;line-height:10.4px}
.field{position:absolute;left:268px;width:98px;height:15px;background:var(--white);color:var(--muted);font-size:4.3px;padding:5px 4px}
.copy{top:1480px;height:20px;background:#141414;color:#bbb;font-size:4.3px;text-align:center;padding-top:8px}
</style>
</head>
<body>
<div class="stage">
<main class="page">

  <div class="section topbar">
    <span style="left:35px">&#9634; BEST CLEANING COMPANY WEBSITE FOREVER!</span>
    <span style="left:374px">&#9719; WORKING HOURS : MON-SAT (8.00AM - 6.00PM)</span>
  </div>

  <header class="section header">
    <div class="brand"><div class="brand-dot"></div><div class="brand-name">Bright Over<br>Dusk Ltd</div></div>
    <svg class="abs" style="left:398px;top:12px" width="7" height="12" viewBox="0 0 7 12"><rect x=".5" y=".5" width="6" height="11" rx="1" fill="none" stroke="#3176b5"/><circle cx="3.5" cy="9.5" r=".7" fill="#3176b5"/></svg>
    <div class="call">CALL TO SCHEDULE YOUR FREE!<b>+(01) 700 555 0190</b></div>
  </header>

  <nav class="section nav">
    <a class="on" style="left:33px">HOME</a><a style="left:71px">ABOUT</a><a style="left:114px">SERVICES</a><a style="left:163px">PROJECTS</a><a style="left:213px">BLOG</a><a style="left:252px">CONTACT US</a>
    <svg class="abs" style="left:476px;top:5px" width="12" height="12" viewBox="0 0 12 12"><circle cx="5" cy="5" r="3.8" fill="none" stroke="#fff" stroke-width="1.6"/><line x1="8" y1="8" x2="11" y2="11" stroke="#fff" stroke-width="1.8"/></svg>
  </nav>

  <section class="section hero">
    <div class="ph" role="img" aria-label="Smiling cleaner holding a sponge and spray bottle" style="left:262px;top:5px;width:150px;height:166px;background:linear-gradient(180deg,#7cc0f1 0%,#d9e8f5 45%,#e6c7d0 100%);opacity:.7"></div>
    <h1>Lorem ipsum dolor<br>consetur adip</h1>
    <svg class="abs" style="left:11px;top:78px" width="8" height="14"><polyline points="7,1 1,7 7,13" fill="none" stroke="#fff" stroke-width="1.3"/></svg>
    <svg class="abs" style="left:502px;top:78px" width="8" height="14"><polyline points="1,1 7,7 1,13" fill="none" stroke="#fff" stroke-width="1.3"/></svg>
  </section>

  <section class="section services">
    <div class="h-sec abs" style="left:34px;top:27px">SERVICE WE OFFER</div>
    <div class="arrow-box" style="left:456px;top:21px"><svg width="5" height="6"><polyline points="4,.5 1,3 4,5.5" fill="none" stroke="#1b1b1b"/></svg></div>
    <div class="arrow-box" style="left:473px;top:21px"><svg width="5" height="6"><polyline points="1,.5 4,3 1,5.5" fill="none" stroke="#1b1b1b"/></svg></div>

    <div class="card" style="left:48px;width:123px">
      <div class="ph" role="img" aria-label="Window squeegee on glass" style="left:13px;top:8px;width:98px;height:74px;background:linear-gradient(135deg,#2d8fd8,#9fd6f6)"></div>
      <p>OFFICE &amp; COMMERCIAL<br>CLEANING</p>
      <div class="btn btn-solid" style="left:29px;top:121px;width:52px;height:11px;line-height:11px">VIEW DETAILS</div>
    </div>
    <div class="card" style="left:186px;width:133px">
      <div class="ph" role="img" aria-label="Cleaner wiping a window frame" style="left:12px;top:8px;width:106px;height:74px;background:linear-gradient(135deg,#8fc8ec,#e8eef2)"></div>
      <p>WINDOWS &amp;<br>UPHOLSTEY CLEANING</p>
      <div class="btn btn-solid" style="left:42px;top:121px;width:52px;height:11px;line-height:11px">VIEW DETAILS</div>
    </div>
    <div class="card" style="left:337px;width:137px">
      <div class="ph" role="img" aria-label="Hand polishing a window with a cloth" style="left:12px;top:8px;width:112px;height:74px;background:linear-gradient(135deg,#6a8a5a,#b9cbd9)"></div>
      <p>HOUSE CLEANING &amp; MAID<br>SERVICE</p>
      <div class="btn btn-solid" style="left:41px;top:121px;width:52px;height:11px;line-height:11px">VIEW DETAILS</div>
    </div>
  </section>

  <section class="section welcome">
    <div class="ph" role="img" aria-label="Illustration of a house with a sponge and spray bottle" style="left:33px;top:86px;width:148px;height:122px;background:linear-gradient(160deg,#eef5fb 0%,#bfe0f3 50%,#f3e4b4 100%);border-radius:6px"></div>
    <h2>WELCOME TO OUR BRIGHT OVER DUSK</h2>
    <p class="tiny abs" style="left:193px;top:75px;width:282px">Lorem ipsum dolor sit amet, consectetur adipiscing elit. Vestibulum interdum fermentum maximus. Sed ferme ntum placerat bibendum. Nunc interdum ac ante vel dictum. Donec quis mauris venenatis, suscipit orci non, mattis dui. Vivamus rhoncus malesuada ultrices. Suspendisse et dolor lectus. Pellentesque pulvinar eleifend dapibus. Suspendisse commodo sagittis sem, eget pulvinar ante fringilla et.</p>
    <div class="btn btn-line" style="left:193px;top:135px;width:52px;height:15px;line-height:13px">ABOUT MORE</div>
    <div class="btn btn-line" style="left:254px;top:135px;width:44px;height:15px;line-height:13px">WORKERS</div>

    <div class="feat" style="left:193px">
      <div class="ic"><svg width="10" height="8"><circle cx="3.5" cy="2.5" r="1.8" fill="none" stroke="#fff" stroke-width=".9"/><path d="M.5 7.5c0-2 1.5-3 3-3s3 1 3 3" fill="none" stroke="#fff" stroke-width=".9"/><circle cx="7" cy="2.5" r="1.4" fill="none" stroke="#fff" stroke-width=".8"/></svg></div>
      <h4>HIGHLY-TRAINED STAFF</h4>
      <p class="tiny">Beatae vitae dicta sunt explicabone seni sal th ipsum voluptatem.</p>
    </div>
    <div class="feat" style="left:290px">
      <div class="ic"><svg width="9" height="9"><line x1="1" y1="1" x2="8" y2="8" stroke="#fff" stroke-width="1.2"/><line x1="8" y1="1" x2="1" y2="8" stroke="#fff" stroke-width="1.2"/></svg></div>
      <h4>QUALITY CLEANING TOOLS</h4>
      <p class="tiny">Beatae vitae dicta sunt explicabone seni sal th ipsum voluptatem.</p>
    </div>
    <div class="feat" style="left:387px">
      <div class="ic"><svg width="9" height="9"><circle cx="4.5" cy="4.5" r="3.6" fill="none" stroke="#fff" stroke-width=".9"/><polyline points="4.5,2.3 4.5,4.7 6,4.7" fill="none" stroke="#fff" stroke-width=".8"/></svg></div>
      <h4>FAST &amp; EFFECTIVE SERVICE</h4>
      <p class="tiny">Beatae vitae dicta sunt explicabone seni sal th ipsum voluptatem.</p>
    </div>
  </section>

  <section class="section staff">
    <div class="h-sec abs" style="left:34px;top:20px">CLEVER STAFFS</div>
    <p class="tiny abs" style="left:57px;top:60px;width:88px;font-size:4.4px">Lorem ipsum dolor sit amet, consectetur adipiscing elit. Vestibu lum interdum fermentum maxi mus. Sed ferme ntum placerat bibendum.</p>
    <div class="arrow-box" style="left:56px;top:115px"><svg width="5" height="6"><polyline points="4,.5 1,3 4,5.5" fill="none" stroke="#1b1b1b"/></svg></div>
    <div class="arrow-box" style="left:73px;top:115px"><svg width="5" height="6"><polyline points="1,.5 4,3 1,5.5" fill="none" stroke="#1b1b1b"/></svg></div>
    <div class="ph" role="img" aria-label="Staff member cleaning a window" style="left:154px;top:31px;width:104px;height:100px;background:linear-gradient(135deg,#f0e8d0,#9fd3f0)"></div>
    <div class="ph" role="img" aria-label="Staff member with a cleaning trolley" style="left:269px;top:31px;width:104px;height:100px;background:linear-gradient(135deg,#c9d8ea,#6c86ad)"></div>
    <div class="ph" role="img" aria-label="Staff member holding cleaning supplies" style="left:384px;top:31px;width:104px;height:100px;background:linear-gradient(135deg,#4f9fe0,#e8b978)"></div>
  </section>

  <section class="section industries">
    <div class="h-sec abs" style="left:35px;top:36px">INDUSTRIES WE SERVE</div>
    <div class="h-sec abs" style="left:285px;top:36px">WHAT OUR CLIENTS SAY</div>
    <p class="tiny abs" style="left:60px;top:66px;width:195px">Architecto beatae vitae dicta sunt explicabo. Nemo eni sal th ipsum voluptatem quia voluptas sit aspernatur aut odit aut fugit dolores eos qui ratione.</p>
    <div class="ind" style="left:60px;top:98px"><svg width="9" height="7"><path d="M1 4h7M5 1l2 3-2 3" fill="none" stroke="#3176b5" stroke-width=".8"/></svg>Airports &amp; Airlines</div>
    <div class="ind" style="left:164px;top:98px"><svg width="9" height="7"><path d="M1 3l3.5-2L8 3 4.5 5z" fill="none" stroke="#3176b5" stroke-width=".8"/></svg>Schools &amp; Universities</div>
    <div class="ind" style="left:60px;top:119px"><svg width="9" height="7"><rect x="1" y="2" width="7" height="3" rx="1" fill="none" stroke="#3176b5" stroke-width=".8"/></svg>Auto Dealerships</div>
    <div class="ind" style="left:164px;top:119px"><svg width="9" height="7"><line x1="1" y1="6" x2="8" y2="1" stroke="#3176b5" stroke-width=".9"/></svg>Medical Facilities</div>
    <div class="ind" style="left:60px;top:140px"><svg width="9" height="7"><path d="M1 2v3M8 2v3M2 3.5h5" fill="none" stroke="#3176b5" stroke-width=".9"/></svg>Sports &amp; Fitness Centers</div>
    <div class="ind" style="left:164px;top:140px"><svg width="11" height="7"><circle cx="2.5" cy="4.5" r="2" fill="none" stroke="#3176b5" stroke-width=".7"/><circle cx="8.5" cy="4.5" r="2" fill="none" stroke="#3176b5" stroke-width=".7"/></svg>Entertainment Venues</div>
    <div class="btn btn-line" style="left:54px;top:158px;width:46px;height:16px;line-height:14px">View More</div>

    <div class="quote">
      <p class="tiny abs" style="left:16px;top:22px;width:112px;font-style:italic">Victa sunt explicabo. Nemo eni sal th ipsum solut voluptatem quia voluptas sit aspernatur aut odit fugit sed quia consequuntur magni dolores volup tas sit aspernatur aut odit aut fugit.</p>
      <div class="abs" style="left:16px;top:73px;font-size:4.6px;font-weight:700">- MARA ELLISON</div>
      <div class="abs tiny" style="left:16px;top:84px">FOUNDER OF XYZ COMPANY</div>
    </div>
    <div class="abs" style="left:496px;top:114px;width:3px;height:3px;border-radius:50%;background:var(--bright)"></div>
    <div class="abs" style="left:496px;top:120px;width:3px;height:3px;border-radius:50%;background:var(--line)"></div>
    <div class="abs" style="left:496px;top:126px;width:3px;height:3px;border-radius:50%;background:var(--line)"></div>
  </section>

  <section class="section news">
    <div class="h-sec abs" style="left:33px;top:20px">LATEST NEWS AND TIPS</div>
    <div class="btn btn-line" style="left:444px;top:25px;width:43px;height:15px;line-height:13px">VIEW ALL</div>
    <article class="post" style="left:39px">
      <div class="flag"></div>
      <h5>12 TIPS TO CLEAN WINDOW</h5>
      <div class="abs tiny" style="left:12px;top:36px;color:var(--bright)">BY ADMIN, &nbsp;LIKES 23</div>
      <p class="tiny abs" style="left:12px;top:48px;width:96px">Neque porro quisquam est, qui thas dolorem ipsum quia dolor sit amets non numquam[...]</p>
      <div class="btn btn-solid" style="left:12px;top:91px;width:43px;height:14px;line-height:14px;background:var(--bright)">READ MORE</div>
      <div class="ph" role="img" aria-label="Smiling cleaner holding a bucket" style="left:109px;top:-10px;width:108px;height:116px;background:linear-gradient(135deg,#e6eef4,#2e6fb6)"></div>
    </article>
    <article class="post" style="left:266px">
      <div class="flag"></div>
      <h5>12 TIPS TO CLEAN WINDOW</h5>
      <div class="abs tiny" style="left:12px;top:36px;color:var(--bright)">BY ADMIN, &nbsp;LIKES 23</div>
      <p class="tiny abs" style="left:12px;top:48px;width:96px">Neque porro quisquam est, qui thas dolorem ipsum quia dolor sit amets non numquam[...]</p>
      <div class="btn btn-solid" style="left:12px;top:91px;width:43px;height:14px;line-height:14px;background:var(--bright)">READ MORE</div>
      <div class="ph" role="img" aria-label="Worker clearing a roof gutter" style="left:108px;top:-10px;width:109px;height:116px;background:linear-gradient(135deg,#5d7a5a,#27406e)"></div>
    </article>
  </section>

  <footer class="section footer">
    <h6 style="left:41px">CONTACTS</h6>
    <div class="row" style="left:41px;top:40px"><svg width="5" height="7"><path d="M2.5 6.5S.5 4 .5 2.5a2 2 0 0 1 4 0C4.5 4 2.5 6.5 2.5 6.5z" fill="#fff"/></svg><span>14 Mersey Row, Unit B<br>Warrington, WA1 2XY</span></div>
    <div class="row" style="left:41px;top:71px"><svg width="6" height="6"><path d="M1 .5l1.3 1.3-.7 1.2 1.4 1.4 1.2-.7L5.5 5 4.6 5.8C2.5 5.5.5 3.5.2 1.4z" fill="#fff"/></svg><span>1-700-555-0147</span></div>
    <div class="row" style="left:41px;top:92px"><svg width="6" height="6"><rect x=".5" y="1" width="5" height="4" fill="#fff"/></svg><span>1-700-555-0183</span></div>

    <h6 style="left:171px">QUICK LINKS</h6>
    <div class="links"><div style="color:#3d9ae8">HOME</div><div>ABOUT</div><div>SERVICES</div><div>PROJECTS</div><div>BLOG</div><div>CONTACT US</div></div>

    <h6 style="left:268px">QUICK CONTACT</h6>
    <div class="field" style="top:41px">Name</div>
    <div class="field" style="top:66px">E - mail</div>
    <div class="btn btn-solid" style="left:268px;top:90px;width:98px;height:15px;line-height:15px;font-weight:400;background:var(--bright)">SUBSCRIBE</div>

    <h6 style="left:403px">FOLLOW US</h6>
    <div class="abs" style="left:404px;top:42px;display:flex;gap:7px">
      <span style="width:5px;height:5px;border-radius:50%;background:var(--bright)"></span>
      <span style="width:5px;height:5px;border-radius:50%;background:#fff"></span>
      <span style="width:5px;height:5px;border-radius:50%;background:#fff"></span>
      <span style="width:5px;height:5px;border-radius:50%;background:#fff"></span>
      <span style="width:5px;height:5px;border-radius:50%;background:#fff"></span>
      <span style="width:5px;height:5px;border-radius:50%;background:#fff"></span>
    </div>
  </footer>
  <div class="section copy">Copyright © . All Rights Reserved</div>

</main>
</div>
</body>
</html>
```